Need Catering Menu designed - design that we want is attached

Hi,
We need a new catering menu designed for our cafe.
I have attached our coffee menu, we would like it to follow the same kind of layout.
It needs to be A4, and can be double sided.
I have attached a word doc of our catering menu, so this is what needs to be on the catering menu you produce.
Also, our contact details need to be on both sides of the menu:
Visit us instore to discuss catering options, or call 0438 672 914 or email marla@tevrostudio.com.au
I have also attached our new logo which I'd like incorporated into the menu
Target Market(s)
Doctors/Nurses
Hospital staff
University Students
Industry/Entity Type
Catering
Look and feel

```html
<!DOCTYPE html>
<html lang="en">
<head>
<meta charset="utf-8">
<title>Ward Round – Catering Menu</title>
<link href="https://fonts.googleapis.com/css2?family=Didact+Gothic&family=Oswald:wght@500&family=Great+Vibes&display=swap" rel="stylesheet">
<style>
:root{
  --ink:#3a2f34;
  --cream:#f5eda6;
  --logo:#f8f2ab;
  --gold:#f2e27a;
  --white:#ffffff;
  --frame:rgba(255,255,255,.85);
  --night:#120f0c;
}
*{margin:0;padding:0;box-sizing:border-box}
html,body{width:1200px;height:845px;overflow:hidden;background:var(--night)}
body{font-family:"Didact Gothic",sans-serif;color:var(--white)}
.menu{position:relative;width:1200px;height:845px;overflow:hidden}
.backdrop{position:absolute;inset:0;
  background:
    radial-gradient(ellipse at 45% 55%,rgba(150,120,60,.55),transparent 60%),
    radial-gradient(ellipse at 80% 25%,rgba(140,105,40,.5),transparent 55%),
    linear-gradient(180deg,#2a2212 0%,#4b3a18 40%,#2c2515 70%,#0f0c08 100%)}
.backdrop-fade{position:absolute;inset:auto 0 0 0;height:140px;background:linear-gradient(180deg,transparent,rgba(0,0,0,.85))}

.brand{position:absolute;left:190px;top:38px;width:210px;height:180px;background:var(--logo);
  display:flex;align-items:center;justify-content:center}
.brand-name{font-family:"Didact Gothic",sans-serif;font-size:24px;letter-spacing:3px;color:var(--ink);text-transform:uppercase}
.menu-title{position:absolute;left:180px;top:226px;width:230px;text-align:center;color:var(--cream);white-space:nowrap}
.menu-title .script{font-family:"Great Vibes",cursive;font-size:26px}
.menu-title .word{font-family:"Didact Gothic",sans-serif;font-size:22px;letter-spacing:4px;font-weight:700}

.panel{position:absolute;border:1.5px solid var(--frame)}
.ribbon{position:absolute;display:flex;align-items:center;justify-content:center}
.ribbon svg{position:absolute;inset:0;width:100%;height:100%}
.ribbon span{position:relative;font-family:"Oswald",sans-serif;color:var(--cream);letter-spacing:1px}

.list{list-style:none}
.list li{display:flex;white-space:nowrap;overflow:hidden}
.list .dots{flex:1;overflow:hidden}
.list .dots::after{content:"........................................................................................................................................................"}
.list .price{padding-left:2px}

.breakfast{left:48px;top:322px;width:485px;height:420px}
.breakfast .list{position:absolute;left:29px;top:52px;width:418px;font-size:19px;line-height:26.4px;letter-spacing:.4px}
.tea{left:665px;top:48px;width:483px;height:366px}
.tea .list{position:absolute;left:56px;top:54px;width:370px;font-size:19px;line-height:26.6px;color:var(--cream);letter-spacing:.4px}
.tea-note{position:absolute;left:0;right:0;text-align:center}
.tea-note.charge{top:318px;font-size:12px;color:var(--gold)}
.tea-note.coffee{top:336px;font-size:15px}

.lunch{left:662px;top:448px;width:236px;height:352px;font-size:6.2px;line-height:7.6px;color:var(--white)}
.lunch .inner{position:absolute;left:9px;top:26px;right:8px}
.lunch .head{display:flex;color:var(--gold);font-size:10px;line-height:12px}
.lunch .head .dots{flex:1;overflow:hidden;white-space:nowrap}
.lunch .head .dots::after{content:"........................................................................."}
.lunch .sub{text-align:center;font-size:6.6px;margin:1px 0 3px}
.lunch b{color:var(--gold)}
.lunch p{margin-bottom:0}

.hot{left:920px;top:448px;width:252px;height:352px}
.hot .list{position:absolute;left:17px;top:34px;width:217px;font-size:10px;line-height:17.2px}

.contact{position:absolute;font-size:10px;line-height:17px}
.contact .hl{color:var(--gold)}
.contact.left{left:15px;top:792px}
.contact.right{left:900px;width:285px;top:777px;text-align:right}
</style>
</head>
<body>
<main class="menu">
  <div class="backdrop" role="img" aria-label="Warm-lit function room with a buffet table of chafing dishes, stacked plates and greenery against patterned wallpaper"></div>
  <div class="backdrop-fade"></div>

  <div class="brand"><span class="brand-name">Ward Round</span></div>
  <div class="menu-title">· <span class="script">Catering</span> <span class="word">MENU</span>·</div>

  <!-- Breakfast -->
  <section class="panel breakfast">
    <ul class="list">
      <li><span>Fruit Platter</span><span class="dots"></span><span class="price">$15</span></li>
      <li><span>Bacon Egg and Cheese Roll</span><span class="dots"></span><span class="price">$6.5</span></li>
      <li><span>Vegetarian Brekky Wrap</span><span class="dots"></span><span class="price">$6.5</span></li>
      <li><span>Ham and Cheese Croissant</span><span class="dots"></span><span class="price">$6</span></li>
      <li><span>Cheese and Tomato Croissant</span><span class="dots"></span><span class="price">$5.5</span></li>
      <li><span>Ham and Cheese French Toast</span><span class="dots"></span><span class="price">$6.5</span></li>
      <li><span>Assorted Yoghurts</span><span class="dots"></span><span class="price">$5.5</span></li>
      <li><span>Bircher Muesli</span><span class="dots"></span><span class="price">$5.5</span></li>
      <li><span>Chia Pudding</span><span class="dots"></span><span class="price">$5.5</span></li>
      <li><span>Granola and Yoghurt</span><span class="dots"></span><span class="price">$5.5</span></li>
      <li><span>Muffin</span><span class="dots"></span><span class="price">$4.5</span></li>
      <li><span>Mini Muffin</span><span class="dots"></span><span class="price">$2.5</span></li>
      <li><span>Juice</span><span class="dots"></span><span class="price">$8</span></li>
    </ul>
  </section>
  <div class="ribbon" style="left:150px;top:300px;width:272px;height:46px">
    <svg viewBox="0 0 272 46" preserveAspectRatio="none"><polygon points="0,0 272,0 258,23 272,46 0,46 14,23" fill="var(--ink)"/><polygon points="0,0 272,0 258,23 272,46 0,46 14,23" fill="none" stroke="#fff" stroke-width="1"/></svg>
    <span style="font-size:29px">BREAKFAST</span>
  </div>

  <!-- Morning and afternoon tea -->
  <section class="panel tea">
    <ul class="list">
      <li><span>Fruit Platter</span><span class="dots"></span><span class="price">$15</span></li>
      <li><span>Muffin</span><span class="dots"></span><span class="price">$4.5</span></li>
      <li><span>Mini Muffin</span><span class="dots"></span><span class="price">$2.5</span></li>
      <li><span>Assorted Slices</span><span class="dots"></span><span class="price">$4</span></li>
      <li><span>Assorted Cookies from</span><span class="dots"></span><span class="price">&nbsp;$3</span></li>
      <li><span>Assorted Yoghurts</span><span class="dots"></span><span class="price">$5.5</span></li>
      <li><span>Chia Pudding</span><span class="dots"></span><span class="price">$5.5</span></li>
      <li><span>Banana Bread</span><span class="dots"></span><span class="price">$4.5</span></li>
      <li><span>Juice</span><span class="dots"></span><span class="price">$8</span></li>
    </ul>
    <p class="tea-note charge">*Cups/Plates/Serviettes can be provided at a charge of $1 per person</p>
    <p class="tea-note coffee">*Barista made coffee available</p>
  </section>
  <div class="ribbon" style="left:697px;top:28px;width:422px;height:44px">
    <svg viewBox="0 0 422 44" preserveAspectRatio="none"><polygon points="0,0 422,0 408,22 422,44 0,44 14,22" fill="var(--ink)" stroke="#fff" stroke-width="1"/></svg>
    <span style="font-size:21px">MORNING and AFTERNOON TEA</span>
  </div>

  <!-- Lunch -->
  <section class="panel lunch">
    <div class="inner">
      <div class="head"><span>Sandwiches or Wraps</span><span class="dots"></span><span>$7.50</span></div>
      <p class="sub">Sandwiches cut into quarters – Wraps cut into thirds</p>
      <p><b>Ham:</b> butter, pickle spread, cheese, tomato, champagne leg ham</p>
      <p style="margin-bottom:3px"><b>Turkey:</b> butter, cranberry sauce, lettuce mix, tomato, turkey breast</p>
      <p><b>Sweet Chilli Chicken:</b></p>
      <p>butter, sweet chilli sauce,</p>
      <p>aioli, lettuce mix, tomato, cheese, sweet chilli chicken tenders</p>
      <p><b>Chicken Schnitzel:</b></p>
      <p>butter, aioli, lettuce mix, tomato, tasty cheese, chicken schnitzel</p>
      <p><b>Egg:</b> butter, lettuce mix, egg, aioli, parsley, spring onion</p>
      <p><b>Tuna:</b> butter, lettuce, tuna, aioli, sundried tomato, spring onion</p>
      <p><b>B.L.T.:</b> butter, aioli, lettuce, tomato, bacon</p>
      <p><b>Salad:</b></p>
      <p>butter, lettuce mix, red onion, cucumber, capsicum,</p>
      <p>tomato, avocado, tasty cheese</p>
      <p><b>Tandoori Chicken:</b> butter, tzatziki, lettuce mix, tomato, tandoori chicken</p>
      <p><b>Waldorf Chicken:</b></p>
      <p>butter, cos lettuce, chicken, seeded mustard, celery, walnuts, aioli</p>
      <p><b>Chicken Caesar:</b></p>
      <p>butter, aioli, cos lettuce, chicken, parmesan cheese, bacon</p>
      <p><b>Cajun Chicken:</b> butter, lettuce mix, tomato, red onion, Cajun chicken</p>
      <p><b>Barbeque Chicken:</b> butter, BBQ,</p>
      <p><b>Felafel:</b></p>
      <div class="head"><span>Foccacias</span><span class="dots"></span><span>$8.50</span></div>
      <p class="sub" style="margin:0">Cut in half – please let us know if you want them toasted</p>
      <p class="sub" style="margin:0">Some options as wraps and sandwiches – Plus:</p>
      <p><b>Roast Veggie:</b> butter, pesto, grilled eggplant, grilled zucchini,</p>
      <p>roasted capsicum, feta cheese, baby spinach, feta cheese, baby spinach</p>
      <p><b>Salami:</b> butter, pesto, baby spinach, mild salami, roasted capsicum,</p>
      <p>olives, feta cheese</p>
      <p><b>Chicken Schnitzel:</b> Butter, housemade coleslaw, chicken schnitzel</p>
      <div class="head"><span>Bagels</span><span class="dots"></span><span>$9.0</span></div>
      <p><b>Turkey:</b> butter, cranberry sauce, baby spinach, tomato, camembert cheese</p>
      <p><b>Smoked Salmon:</b> butter, cream cheese, baby spinach, tomato, smoked salmon</p>
    </div>
  </section>
  <div class="ribbon" style="left:680px;top:428px;width:212px;height:40px">
    <svg viewBox="0 0 212 40" preserveAspectRatio="none"><polygon points="0,0 212,0 200,20 212,40 0,40 12,20" fill="var(--ink)" stroke="#fff" stroke-width="1"/></svg>
    <span style="font-size:25px">LUNCH</span>
  </div>

  <!-- Hot food -->
  <section class="panel hot">
    <ul class="list">
      <li><span>Assorted Pies</span><span class="dots"></span><span class="price">$5.0</span></li>
      <li><span>Large tray hot chips</span><span class="dots"></span><span class="price">$15</span></li>
      <li><span>Small tray hot chips</span><span class="dots"></span><span class="price">$9</span></li>
      <li><span>Mini samosa</span><span class="dots"></span><span class="price">$3</span></li>
      <li><span>Vegetarian spring rolls</span><span class="dots"></span><span class="price">$3</span></li>
      <li><span>Vegetarian spring rolls</span><span class="dots"></span><span class="price">$3</span></li>
      <li><span>Mini sausage rolls</span><span class="dots"></span><span class="price">$3</span></li>
      <li><span>Mini quiche</span><span class="dots"></span><span class="price">$3</span></li>
      <li><span>Mini dim sim</span><span class="dots"></span><span class="price">$2</span></li>
      <li><span>Sweet chilli chicken tenders</span><span class="dots"></span><span class="price">$3</span></li>
      <li><span>Meatballs</span><span class="dots"></span><span class="price">$2</span></li>
      <li><span>Spinach and ricotta pastizi</span><span class="dots"></span><span class="price">$3</span></li>
      <li><span>Vegetarian Frittata</span><span class="dots"></span><span class="price">$4.5</span></li>
      <li><span>Meat Frittata</span><span class="dots"></span><span class="price">$4.5</span></li>
    </ul>
  </section>
  <div class="ribbon" style="left:972px;top:430px;width:155px;height:36px">
    <svg viewBox="0 0 155 36" preserveAspectRatio="none"><polygon points="0,0 155,0 144,18 155,36 0,36 11,18" fill="var(--ink)" stroke="#fff" stroke-width="1"/></svg>
    <span style="font-size:23px;letter-spacing:0">Hot Food</span>
  </div>

  <p class="contact left">Visit us instore to discuss catering options,<br>&nbsp;or call <span class="hl">0438 672 914</span> or email <span class="hl">marla@tevrostudio.com.au</span></p>
  <p class="contact right">Visit us instore to discuss catering options,<br>or call <span class="hl">0438 672 914</span> or email <span class="hl">marla@tevrostudio.com.au</span></p>
</main>
</body>
</html>
```